BOLD & MINIMALIST DESIGN NEEDED

We want a very bold but minimalistic business card design that is impactful and utilizes both sides of the business card. Our current logo is included for your use.

We want bold fonts and good use of negative space. We don't want the logo to overpower the design.

Target Market(s)

Professionals who are building new commercial buildings.

Industry/Entity Type

Construction

Contact Information for Business Card

Name, Title, email, office phone, cell phone, website

Font styles to use
Serif
Sans Serif

Requirements
Must have
• Bold design!

```html
<!DOCTYPE html>
<html lang="en">
<head>
<meta charset="utf-8">
<title>Ridgeway Design + Build — Business Card</title>
<link href="https://fonts.googleapis.com/css2?family=Montserrat:wght@400;500;700;800&display=swap" rel="stylesheet">
<style>
  :root {
    --page-bg: #eceff1;
    --card-bg: #ffffff;
    --ink: #1d1d1b;
    --ink-soft: #555555;
    --accent: #7cc242;
    --card-shadow: rgba(0, 0, 0, 0.12);
  }
  * { box-sizing: border-box; margin: 0; padding: 0; }
  html, body {
    width: 1200px;
    height: 686px;
    overflow: hidden;
    background: var(--page-bg);
    font-family: "Montserrat", sans-serif;
    color: var(--ink);
  }
  .card-set {
    width: 1200px;
    height: 686px;
    display: flex;
    align-items: center;
    justify-content: center;
    gap: 60px;
  }
  .card {
    position: relative;
    width: 490px;
    height: 280px;
    background: var(--card-bg);
    box-shadow: 0 8px 24px var(--card-shadow);
    overflow: hidden;
  }

  /* Front: contact side */
  .contact-block {
    position: absolute;
    top: 52px;
    left: 210px;
  }
  .contact-name {
    font-weight: 800;
    font-size: 22px;
    letter-spacing: 1px;
    text-transform: uppercase;
  }
  .contact-title {
    margin-top: 4px;
    font-weight: 500;
    font-size: 10px;
    letter-spacing: 3.5px;
    text-transform: uppercase;
    color: var(--ink-soft);
  }
  .contact-lines {
    margin-top: 16px;
    list-style: none;
    font-size: 9.5px;
    line-height: 1.55;
    letter-spacing: 0.8px;
    color: var(--ink-soft);
  }
  .front-brand {
    position: absolute;
    left: 30px;
    bottom: 52px;
    display: flex;
    align-items: center;
    gap: 8px;
  }
  .brand-square {
    width: 14px;
    height: 14px;
    background: var(--accent);
  }
  .brand-name {
    font-weight: 800;
    font-size: 18px;
    letter-spacing: 1px;
    text-transform: uppercase;
    color: var(--ink);
  }
  .base-curve {
    position: absolute;
    left: 0;
    bottom: 0;
    width: 490px;
    height: 60px;
  }

  /* Back: brand side */
  .card-back {
    display: flex;
    flex-direction: column;
    align-items: center;
    justify-content: center;
  }
  .back-brand {
    display: flex;
    flex-direction: column;
    align-items: center;
    gap: 6px;
  }
  .back-brand .brand-square {
    width: 22px;
    height: 22px;
  }
  .back-brand .brand-name {
    font-size: 30px;
    letter-spacing: 1.5px;
  }
  .brand-tagline {
    font-weight: 700;
    font-size: 11px;
    letter-spacing: 5px;
    text-transform: uppercase;
    color: var(--ink);
  }
  .website {
    margin-top: 34px;
    font-weight: 700;
    font-size: 10px;
    letter-spacing: 2px;
    text-transform: uppercase;
  }
</style>
</head>
<body>
  <main class="card-set">
    <section class="card card-front" aria-label="Business card front">
      <div class="contact-block">
        <h1 class="contact-name">Sample Name</h1>
        <p class="contact-title">Managing Director</p>
        <ul class="contact-lines">
          <li>Office 555 010 2040</li>
          <li>Cell 555 010 3070</li>
          <li>name@ridgewaybuild.com</li>
        </ul>
      </div>
      <div class="front-brand">
        <span class="brand-square"></span>
        <span class="brand-name">Ridgeway</span>
      </div>
      <svg class="base-curve" viewBox="0 0 490 60" preserveAspectRatio="none" aria-hidden="true">
        <path d="M0 40 Q245 22 490 46" fill="none" stroke="var(--ink)" stroke-width="1.5"/>
      </svg>
    </section>

    <section class="card card-back" aria-label="Business card back">
      <div class="back-brand">
        <span class="brand-square"></span>
        <span class="brand-name">Ridgeway</span>
        <span class="brand-tagline">Design + Build</span>
      </div>
      <p class="website">www.ridgewaybuild.com</p>
    </section>
  </main>
</body>
</html>
```